Contemporary Literature/Novel Needs Book Cover Design

This fiction novel is entitled "Before the Tide Turns".
This is a literary fiction piece of work, with the protagonist a female mathematician. The general precis of the novel is her life and her overriding sentimentality that everything on Earth - all life, all memories, all love, all of the events we ever experienced, will all vanish without a trace when the sun dies. I am looking for a classic looking book cover in keeping with the literary feel of the novel, but also something that ties in the mathematics / astronomy of the protagonist's work, and of course the actual title of the book.
The protagonist is a female, the book covers the period of her life from 20 years of age to the late 40's. By "Classic" look I mean: expensive and timeless; something that could have been written 100 years ago, or today.
Please contact me for any further clarifications.
Updates

Reason: Extending deadline to allow for the Easter holiday period as I will b e offline for the next 2 days.

Target Market(s)

Contemporary literature buyers

Industry/Entity Type

Work

Font styles to use
Script

Requirements
Must have
• Cover design that reflects the brief / precis of the novel.
• Author: R.K Fenwick
Should not have
• Images of people

```html
<!DOCTYPE html>
<html lang="en">
<head>
<meta charset="utf-8">
<title>Before the Tide Turns — R.K Fenwick</title>
<link rel="stylesheet" href="https://fonts.googleapis.com/css2?family=Cinzel:wght@400;500&display=swap">
<style>
  :root {
    --sky-top: #4f5f72;
    --sky-blue: #8fa3b2;
    --sun-glow: #f0a85a;
    --sun-core: #fbe3a8;
    --cloud: #6a5a58;
    --haze: #d8b27c;
    --mist: #c49462;
    --field: #8a6a48;
    --ground: #4a3a2c;
    --ink: #3a2a1e;
    --title-cream: #fbf1c4;
    --text-shadow: rgba(60, 35, 15, 0.75);
    --ornament: #e0902e;
  }
  * { margin: 0; padding: 0; box-sizing: border-box; }
  html, body {
    width: 800px;
    height: 1200px;
    overflow: hidden;
    background: var(--ground);
  }
  .cover {
    position: relative;
    width: 800px;
    height: 1200px;
    overflow: hidden;
    font-family: "Cinzel", "Times New Roman", serif;
    color: var(--title-cream);
  }
  .cover-scene {
    position: absolute;
    inset: 0;
    background:
      radial-gradient(ellipse 260px 90px at 400px 360px, var(--sun-core) 0%, rgba(242,183,102,0.6) 45%, rgba(242,183,102,0) 100%),
      radial-gradient(ellipse 520px 120px at 400px 250px, rgba(240,150,70,0.8) 0%, rgba(240,150,70,0) 100%),
      radial-gradient(ellipse 760px 460px at 420px 520px, rgba(245,210,150,0.7) 0%, rgba(216,178,124,0) 70%),
      linear-gradient(180deg,
        var(--sky-top) 0%,
        var(--sky-blue) 8%,
        #c99c6f 16%,
        var(--sun-glow) 22%,
        var(--cloud) 29%,
        #b99070 33%,
        var(--haze) 40%,
        #d9b583 50%,
        var(--mist) 62%,
        var(--field) 80%,
        var(--ground) 100%);
  }
  .equation-field {
    position: absolute;
    left: 0;
    right: 0;
    top: 700px;
    bottom: 0;
    background:
      repeating-linear-gradient(180deg, rgba(58,42,30,0) 0px, rgba(58,42,30,0) 30px, rgba(58,42,30,0.10) 31px, rgba(58,42,30,0.10) 44px, rgba(58,42,30,0) 45px, rgba(58,42,30,0) 60px),
      linear-gradient(180deg, rgba(58,42,30,0) 0%, rgba(58,42,30,0.18) 40%, rgba(58,42,30,0.35) 100%);
    -webkit-mask-image: linear-gradient(180deg, transparent 0%, #000 30%);
            mask-image: linear-gradient(180deg, transparent 0%, #000 30%);
  }
  .title-line {
    position: absolute;
    left: 0;
    right: 0;
    text-align: center;
    font-weight: 400;
    line-height: 1;
    white-space: nowrap;
    text-shadow: 0 2px 6px var(--text-shadow), 0 0 2px rgba(60,35,15,0.5);
  }
  .title-lead {
    top: 515px;
    font-size: 53px;
    letter-spacing: 3px;
  }
  .title-middle {
    top: 576px;
    font-size: 150px;
    letter-spacing: 2px;
  }
  .title-last {
    top: 741px;
    font-size: 185px;
    letter-spacing: 2px;
  }
  .ornament {
    position: absolute;
    left: 316px;
    top: 925px;
    width: 170px;
    height: 60px;
    border-radius: 30px;
    background: radial-gradient(ellipse at center, var(--ornament) 0%, rgba(224,144,46,0.55) 50%, rgba(224,144,46,0.1) 100%);
  }
  .author {
    position: absolute;
    left: 0;
    right: 0;
    top: 1041px;
    text-align: center;
    font-size: 62px;
    line-height: 1;
    font-weight: 500;
    letter-spacing: 9px;
    font-variant: small-caps;
    white-space: nowrap;
    text-shadow: 0 2px 5px var(--text-shadow);
  }
</style>
</head>
<body>
  <main class="cover">
    <div class="cover-scene" role="img" aria-label="Sunrise over a misty field with a row of trees casting long light rays"></div>
    <div class="equation-field" role="img" aria-label="Faint handwritten mathematical equations and calculations spread across the lower field"></div>

    <h1 class="title">
      <span class="title-line title-lead">BEFORE THE</span>
      <span class="title-line title-middle">TIDE</span>
      <span class="title-line title-last">TURNS</span>
    </h1>

    <div class="ornament" role="img" aria-label="Orange calligraphic flourish ornament"></div>

    <p class="author">R.K Fenwick</p>
  </main>
</body>
</html>
```